Velvet Harbor Nose Picks - our own unique product line of cotton swabs

We have something now that we are not too happy with. Looking to create a label for a line of cotton swabs that we have created and designed to clean your nose from mucus and boogers. The logo that i have so far for the packaging is the white background with the black silhouette nose (attached). We need something that can do well in the retail/consumer market. Our website address (even though it is not live yet) should be listed somewhere on the label....
www.VelvetHarbor-example.com ( we sell pillows, but we have other product lines)
We would also like to see a brief description on how to correctly use the nose pick on the back side of the label. The description on how to use should read " insert cotton nose pick into nostril and give it a few counter clock wise twirls or till you feel mucus/debris latch onto the cotton. You may need to repeat the process and use more than one nose pick to achieve desired result."
As well as a warning mentioning : "Never insert plastic end of nose pick into any part of your body. Be careful and use with caution."
Also for you to know, the cotton is made from 100% natural cotton, the cotton head itself is thick and highly absorbent making it a pleasure to use. There are 50 nose picks per pack.
We're fine with keeping it simple and not making the packaging too busy, however we're open to your ideas and designs! I have given you the most important information relevant to the project. If there are any questions or something is not clear enough please kindly message me.

Requirements
Must have
• professional looking
clean looking
not busy
Should not have
• words clumping together making it appear as too much text in one area
too much text clumped together on the design

```html
<!DOCTYPE html>
<html lang="en">
<head>
<meta charset="utf-8">
<title>Velvet Harbor Nose Picks – Cotton Swabs Label</title>
<link rel="stylesheet" href="https://fonts.googleapis.com/css2?family=Bebas+Neue&family=Montserrat:wght@300;400;500;700&display=swap">
<style>
  :root {
    --page: #ffffff;
    --sky: #86cdea;
    --sky-deep: #7cc7e7;
    --cloud: #eef7fc;
    --ink: #111111;
    --pill: #383a3c;
    --pill-text: #9fd8f0;
    --panel: #ffffff;
  }
  * { margin: 0; padding: 0; box-sizing: border-box; }
  html, body {
    width: 1200px; height: 1001px; overflow: hidden;
    background: var(--page);
    font-family: "Montserrat", sans-serif;
    color: var(--ink);
  }
  .label {
    position: absolute; left: 74px; top: 307px;
    width: 1052px; height: 352px; overflow: hidden;
    background:
      radial-gradient(ellipse 260px 40px at 470px 20px, rgba(255,255,255,.75), transparent 70%),
      radial-gradient(ellipse 420px 150px at 520px 330px, rgba(255,255,255,.85), transparent 70%),
      radial-gradient(ellipse 300px 120px at 900px 320px, rgba(255,255,255,.7), transparent 70%),
      radial-gradient(ellipse 200px 80px at 900px 40px, rgba(255,255,255,.45), transparent 70%),
      linear-gradient(180deg, var(--sky) 0%, var(--sky-deep) 55%, #b9e1f3 100%);
  }
  .cotton-art {
    position: absolute; left: 0; top: 76px; width: 303px; height: 276px;
    background: radial-gradient(ellipse at 45% 55%, rgba(255,255,255,.55), rgba(134,205,234,0) 70%);
  }
  .center { position: absolute; left: 0; width: 1052px; text-align: center; }
  .brand {
    top: 50px; font-weight: 500; font-size: 17px; letter-spacing: .3px; line-height: 1.2;
  }
  .brand-mark {
    display: inline-block; width: 10px; height: 10px; border-radius: 50%;
    background: var(--ink); margin-right: 8px; vertical-align: 1px;
  }
  .title {
    top: 124px; font-family: "Bebas Neue", sans-serif; font-size: 58px;
    letter-spacing: 1px; line-height: 1;
  }
  .count {
    position: absolute; left: 419px; top: 188px; width: 210px; height: 30px;
    border-radius: 15px; background: var(--pill); color: var(--pill-text);
    font-weight: 300; font-size: 20px; line-height: 30px; text-align: center;
  }
  .cotton-badge { position: absolute; left: 457px; top: 247px; display: flex; gap: 5px; }
  .cotton-badge .frame { width: 37px; height: 38px; border: 1px solid var(--ink); }
  .cotton-badge p { font-size: 10px; line-height: 12px; margin-top: 1px; }
  .cotton-badge strong { font-weight: 700; font-size: 11.5px; }
  .url { top: 308px; font-size: 12px; letter-spacing: .2px; }
  .info {
    position: absolute; left: 754px; width: 246px; text-align: center;
    font-size: 11.2px; line-height: 13.2px;
  }
  .info h2 {
    font-size: 11.5px; font-weight: 700; margin: 0 40px 5px -20px;
    padding-bottom: 2px; border-bottom: 1px solid var(--ink); width: 286px;
    margin-left: -20px;
  }
  .how { top: 51px; }
  .caution { top: 167px; }
  .note-panel {
    position: absolute; left: 817px; top: 242px; width: 120px; height: 52px;
    background: var(--panel); border: 1px solid #555;
  }
</style>
</head>
<body>
  <main class="label">
    <div class="cotton-art" role="img" aria-label="Line drawing of cotton bolls on stems"></div>

    <div class="center brand"><span class="brand-mark"></span>Velvet Harbor Nose Picks</div>
    <h1 class="center title">COTTON SWABS</h1>
    <div class="count">50 NOSE PICKS</div>

    <div class="cotton-badge">
      <div class="frame"></div>
      <p>MADE WITH<br><strong>100% NATURAL<br>COTTON</strong></p>
    </div>

    <div class="center url">www.VelvetHarbor-example.com</div>

    <section class="info how">
      <h2>HOW TO USE:</h2>
      <p>insert cotton nose pick into nostril and give it a few counter clock wise twirls or till you feel mucus/debris latch onto the cotton. You may need to repeat the process and use more than one nose pick to achieve desired result.</p>
    </section>
    <section class="info caution">
      <h2>CAUTION:</h2>
      <p>Never insert plastic end of nose pick into any part of your body. Be careful and use with caution.</p>
    </section>
    <div class="note-panel"></div>
  </main>
</body>
</html>
```